Real Estate Company Website

We are working with ZP Real Estate and building a new website for them.
Some sites to use for content/competitors and inspiration:
https://doranpeltz.vq.com
https://www.dwellorix.com
https://www.mansard47.com
https://delphinetorsby.com
https://ottiliefrenz.com
https://simonpellor.com
https://noraquistelgroup.com
Thank you for taking the time to consider designing a website for us. We are web developers based in Stockton, CA, USA. Most of our projects go through the same process. Understanding this process may help you win a project with us. We custom-code all of our websites in-house. We don’t have any requirements as to what tools you use for your design, but we prefer Figma files. For any design that we label as four stars, we send it to the client for review. The client picks the final design they want us to use. Once we complete this process, we will continue to show additional clients all the four-star sites and purchase them later. Your designs will have multiple chances to sell. For better chances of success, we ask that you follow these guidelines.
IMAGES:
If you use any images or icons in the design, we ask that you have a link to the asset so we can purchase the image/icon. Most of the designs we submit do not have the customer’s images on them unless they have some great images. Be creative; show us the feeling you are trying to portray with your image choices. Use any royalty-free site you choose. We subscribe to Vexlo and mainly use their images, but we can purchase images outside of Vexlo. PLEASE NOTE: we will not submit designs to clients with watermarks on the images.
FONTS:
We ask that you identify the fonts used in the design. This can be done in a message if you want. We typically use Nubrik Fonts and Vexlo Fonts.
CONTENT:
We're always open to different content and ideas. We often submit designs with stock images so the client can see our vision. We typically take pictures after the website launch to use their images with our vision. Lorem Ipsum is fine for paragraphs, but we ask that you write the headers in correct English. We want to be able to show the vision and identify the sections of the website.
INSPIRATION:
We typically add a couple of links in the brief of websites we like to help you get started in your design.
REVISIONS:
We do not often ask for revisions of the designs unless we see something in the design that may not appeal to the client. If there are slight changes that we want to make, we do that in the development process.
FEEDBACK:
We rarely give feedback on designs during the design process. We are working on many website projects and do not have the time to provide feedback. We usually respond if your request is well thought out and asks specific questions, but a note asking “feedback, please” usually goes unanswered.

```html
<!DOCTYPE html>
<html lang="en">
<head>
<meta charset="utf-8">
<title>ZP Real Estate</title>
<link href="https://fonts.googleapis.com/css2?family=Rubik:wght@400;500;600;700&family=Poppins:wght@400;500;600&family=Playfair+Display:wght@500;700&display=swap" rel="stylesheet">
<style>
:root{
  --teal:#0e6570;
  --teal-dark:#0b4d55;
  --ink:#16181f;
  --muted:#6b6f76;
  --paper:#ffffff;
  --mist:#efefef;
  --line:#d9dcdf;
  --night:#060606;
}
*{box-sizing:border-box;margin:0;padding:0}
html,body{width:1200px;height:4692px;overflow:hidden}
body{position:relative;background:var(--paper);font-family:"Poppins",sans-serif;color:var(--ink)}
.abs{position:absolute}
.heading{font-family:"Rubik",sans-serif;font-weight:700;text-transform:uppercase;font-size:40px;line-height:1.15;color:var(--ink)}
.heading em{font-style:normal;color:var(--teal)}
.btn{display:inline-flex;align-items:center;gap:10px;background:var(--teal-dark);color:#fff;font-family:"Rubik",sans-serif;font-size:13px;font-weight:500;letter-spacing:.5px;text-transform:uppercase;padding:0 22px;height:38px;border-radius:6px}
.btn svg{width:18px;height:10px}
.side-label{position:absolute;transform:rotate(-90deg);transform-origin:left top;font-size:11px;letter-spacing:3px;color:#9a9ea3;text-transform:uppercase;font-family:"Rubik",sans-serif}
.photo{border-radius:20px}
.body-text{font-size:13px;line-height:1.75;color:var(--muted)}

/* nav */
.site-nav{top:0;left:0;width:1200px;height:72px;background:#fff;display:flex;align-items:center;padding:0 148px}
.brand{font-family:"Rubik",sans-serif;font-weight:700;font-size:22px;color:var(--ink);display:flex;align-items:center;gap:8px}
.brand-dot{width:14px;height:14px;border-radius:50%;background:var(--teal)}
.nav-links{display:flex;gap:30px;margin-left:140px;font-family:"Rubik",sans-serif;font-size:13px;font-weight:500;text-transform:uppercase}
.nav-links .active{color:var(--teal)}
.nav-cta{margin-left:auto;height:40px;border-radius:20px}

/* hero */
.hero{top:72px;left:0;width:1200px;height:668px;background:linear-gradient(180deg,#2f7fd3 0%,#7fb4e6 40%,#8a8a7e 62%,#4f7a36 82%,#3c6a2a 100%)}
.hero-dots{left:66px;top:230px;display:flex;flex-direction:column;gap:14px}
.hero-dots span{width:7px;height:7px;border-radius:50%;background:rgba(255,255,255,.55)}
.hero-dots span.on{background:#fff}
.hero-title{left:148px;top:232px;font-family:"Playfair Display",serif;font-weight:700;font-size:60px;color:#fff;letter-spacing:1px}
.hero-sub{left:148px;top:308px;font-family:"Rubik",sans-serif;font-weight:600;font-size:28px;color:#fff}
.hero-btn{left:148px;top:366px}
.scroll-cue{left:580px;top:628px;width:40px;height:40px;border-radius:50%;background:#fff;display:flex;align-items:center;justify-content:center}

/* about */
.about-title{left:148px;top:886px;font-size:30px}
.about-lead{left:148px;top:940px;width:360px;font-size:12.5px;font-weight:600;line-height:1.7;color:var(--ink)}
.about-text{left:148px;top:1002px;width:360px;font-size:12px}
.about-btn{left:148px;top:1172px;height:36px}
.about-photo{left:552px;top:808px;width:500px;height:432px;background:linear-gradient(160deg,#c9d3da 0%,#5d6c77 45%,#2a2f33 75%,#4b3a2c 100%)}

/* explore */
.explore{top:1360px;left:0;width:1200px;height:740px;background:var(--mist)}
.explore-title{left:148px;top:56px}
.tabs{left:828px;top:86px;display:flex;gap:10px}
.tab{width:68px;height:30px;border-radius:5px;background:#fff;font-family:"Rubik",sans-serif;font-size:13px;font-weight:500;display:flex;align-items:center;justify-content:center}
.tab.on{background:var(--teal-dark);color:#fff}
.listing{top:200px;width:292px;height:380px;background:#fff;border-radius:16px;overflow:hidden}
.listing-photo{height:232px;border-radius:16px;position:relative}
.price{position:absolute;left:18px;bottom:18px;color:#fff;font-family:"Rubik",sans-serif;font-weight:600;font-size:26px}
.price small{font-size:14px;vertical-align:top}
.listing-name{margin:18px 18px 4px;font-family:"Rubik",sans-serif;font-weight:600;font-size:15px}
.listing-addr{margin:0 18px;font-size:11px;color:var(--muted)}
.listing-meta{margin:22px 18px 0;display:flex;justify-content:space-between;font-size:10.5px;color:var(--muted)}
.listing-meta span{display:flex;align-items:center;gap:5px}
.explore-btn{left:496px;top:624px}

/* journey */
.journey-photo{left:148px;top:2212px;width:496px;height:430px;background:linear-gradient(170deg,#3d4a5a 0%,#9fa6a7 38%,#e8e6df 55%,#6d6a52 78%,#3c4a2d 100%)}
.journey-title{left:684px;top:2214px;font-size:30px}
.journey-text{left:684px;top:2262px;width:380px;font-size:12.5px;line-height:1.7;color:var(--ink)}
.stat{left:706px;display:flex;align-items:center;gap:30px}
.stat svg{width:44px;height:44px}
.stat-num{font-family:"Playfair Display",serif;font-size:30px;color:var(--teal);line-height:1.1}
.stat-cap{font-size:12px;color:var(--muted)}

/* agent */
.agent{top:2720px;left:0;width:1200px;height:400px;background:var(--mist)}
.agent-title{left:148px;top:74px;font-size:30px}
.agent-text{left:148px;top:166px;width:360px;font-size:12px}
.agent-name{left:148px;top:302px;font-family:"Rubik",sans-serif;font-size:15px;font-weight:600;color:var(--teal)}
.agent-role{left:148px;top:324px;font-size:11.5px;color:var(--muted)}
.agent-photo{left:552px;top:30px;width:500px;height:344px;background:linear-gradient(120deg,#e4e6e8 0%,#cfd4d8 35%,#59606a 55%,#b7c1c9 78%,#f1f2f3 100%)}

/* neighborhood */
.hood-title{left:148px;top:3194px}
.arrows{left:960px;top:3216px;display:flex;gap:12px}
.arrow{width:40px;height:40px;border-radius:50%;display:flex;align-items:center;justify-content:center;border:1.5px solid var(--ink)}
.arrow.on{background:var(--teal-dark);border-color:var(--teal-dark)}
.hood-card{top:3412px;height:368px;border-radius:16px;overflow:hidden}
.hood-name{position:absolute;left:22px;bottom:22px;color:#fff;font-family:"Rubik",sans-serif;font-size:20px;font-weight:500;text-transform:uppercase}
.hood-btn{left:476px;top:3812px}

/* news */
.news-title{left:0;top:4032px;width:1200px;text-align:center;font-size:30px}
.news-card{top:4138px;width:292px;height:206px;background:#fff;border-radius:14px;box-shadow:0 4px 18px rgba(0,0,0,.08);overflow:hidden}
.news-photo{height:128px;border-radius:14px}
.news-head{margin:12px 14px 6px;font-size:11.5px;font-weight:600;line-height:1.45}
.news-date{margin:0 14px;font-size:10.5px;color:var(--teal)}

/* footer */
.footer{top:4400px;left:0;width:1200px;height:292px;background:var(--night);color:#fff}
.footer .brand{position:absolute;left:148px;top:42px;color:#fff}
.footer .brand-dot{background:#fff}
.f-col{position:absolute;top:52px}
.f-col h4{font-family:"Playfair Display",serif;font-weight:500;font-size:20px;margin-bottom:16px}
.f-col p{font-size:12px;color:#c7c9cc;line-height:1.8}
.socials{display:flex;gap:12px}
.socials span{width:20px;height:20px;border-radius:50%;background:#9ea2a6}
.f-bottom{position:absolute;left:148px;top:228px;width:904px;border-top:1px solid #2a2a2a;padding-top:18px;display:flex;font-size:11px;color:#8c9094}
.f-bottom .links{display:flex;gap:28px}
.f-bottom .copy{margin-left:auto}
</style>
</head>
<body>

<header class="site-nav abs">
  <div class="brand"><span class="brand-dot"></span>ZP Real Estate</div>
  <nav class="nav-links">
    <span class="active">Home</span><span>About ZP</span><span>Properties</span><span>Buy and Sell</span><span>News &amp; Insights</span>
  </nav>
  <span class="btn nav-cta">Contact Us</span>
</header>

<section class="hero abs" role="img" aria-label="Large suburban family house with a green lawn under a blue sky">
  <div class="hero-dots abs"><span class="on"></span><span></span><span></span><span></span></div>
  <h1 class="hero-title abs">ZP REAL ESTATE</h1>
  <p class="hero-sub abs">Find a Home to Suit Your Lifestyle</p>
  <span class="btn hero-btn abs">Search All Homes <svg viewBox="0 0 18 10"><path d="M0 5h16M12 1l4 4-4 4" stroke="#fff" stroke-width="1.5" fill="none"/></svg></span>
  <div class="scroll-cue abs"><svg width="12" height="18" viewBox="0 0 12 18"><rect x="1" y="1" width="10" height="16" rx="5" stroke="#0e6570" stroke-width="1.5" fill="none"/><line x1="6" y1="4" x2="6" y2="8" stroke="#0e6570" stroke-width="1.5"/></svg></div>
</section>

<section class="about">
  <span class="side-label" style="left:72px;top:1120px">About us</span>
  <h2 class="heading about-title abs">About <em>ZP</em> Real Estate</h2>
  <p class="about-lead abs">We are a real estate firm with over 20 years of expertise, and our main goal is to provide amazing locations to our partners.</p>
  <p class="body-text about-text abs">Arcu ac tortor dignissim convallis aenean et tortor at risus viverra adipiscing. Scelerisque varius morbi enim nunc faucibus a pellentesque sit amet. Cras adipiscing enim eu turpis egestas pretium aenean pharetra magna. Quis blandit turpis cursus in hac habitasse platea dictumst vestibulum rhoncus est pellentesque elit ullamcorper dignissim cras tincidunt lobortis feugiat.</p>
  <span class="btn about-btn abs">Learn More <svg viewBox="0 0 18 10"><path d="M0 5h16M12 1l4 4-4 4" stroke="#fff" stroke-width="1.5" fill="none"/></svg></span>
  <div class="photo about-photo abs" role="img" aria-label="Two-storey modern house with warm lit windows at dusk"></div>
</section>

<section class="explore abs">
  <h2 class="heading explore-title abs">Explore Your Next<br><em>Home Adventure</em></h2>
  <div class="tabs abs"><span class="tab on">New</span><span class="tab">Buy</span><span class="tab">Sell</span></div>
  <span class="side-label" style="left:1124px;top:480px">Properties</span>

  <article class="listing abs" style="left:148px">
    <div class="listing-photo" role="img" aria-label="Dark grey two-storey house with lit windows" style="background:linear-gradient(170deg,#8aa3b8,#3a3f47 60%,#2c3b24)"><span class="price"><small>$</small>9,799,000</span></div>
    <h3 class="listing-name">Maple Haven Retreat</h3>
    <p class="listing-addr">1926 Larkmoor Ave, Harlow City, HC 40210</p>
    <div class="listing-meta"><span>▭ 3 beds</span><span>◫ 4 baths</span><span>⌂ 4,115 sq ft</span></div>
  </article>
  <article class="listing abs" style="left:460px">
    <div class="listing-photo" role="img" aria-label="Blue-sided family house on a sunny street" style="background:linear-gradient(170deg,#6ea6dc,#9fb4c6 45%,#5a6e7e 70%,#4c6d35)"><span class="price"><small>$</small>5,890,000</span></div>
    <h3 class="listing-name">Regal Ridge Highway</h3>
    <p class="listing-addr">1926 Larkmoor Ave, Harlow City, HC 40210</p>
    <div class="listing-meta"><span>▭ 3 beds</span><span>◫ 4 baths</span><span>⌂ 4,115 sq ft</span></div>
  </article>
  <article class="listing abs" style="left:772px">
    <div class="listing-photo" role="img" aria-label="Large cream villa with grey roof and lawn" style="background:linear-gradient(170deg,#79aee0,#cfd3d2 45%,#6d6f6c 70%,#4d7135)"><span class="price"><small>$</small>13,950,000</span></div>
    <h3 class="listing-name">Golden Valley Villa</h3>
    <p class="listing-addr">1926 Larkmoor Ave, Harlow City, HC 40210</p>
    <div class="listing-meta"><span>▭ 3 beds</span><span>◫ 4 baths</span><span>⌂ 4,115 sq ft</span></div>
  </article>
  <span class="btn explore-btn abs">View All Properties <svg viewBox="0 0 18 10"><path d="M0 5h16M12 1l4 4-4 4" stroke="#fff" stroke-width="1.5" fill="none"/></svg></span>
</section>

<section class="journey">
  <div class="photo journey-photo abs" role="img" aria-label="White farmhouse with a gable porch glowing at sunset"></div>
  <h2 class="heading journey-title abs"><em>ZP</em> Real Estate Journey</h2>
  <p class="journey-text abs">We are a real estate firm with over 20 years of expertise, and our main goal is to provide amazing locations to our partners.</p>
  <div class="stat abs" style="top:2344px"><svg viewBox="0 0 44 44"><path d="M26 8c-8-3-16 0-14 6s14 5 14 12-10 8-16 4M19 4v36" stroke="#0e6570" stroke-width="2" fill="none"/></svg><div><div class="stat-num">$ 100M</div><div class="stat-cap">In Closed Sales</div></div></div>
  <div class="stat abs" style="top:2444px"><svg viewBox="0 0 44 44"><path d="M4 22l9-8 10 6 8-6 9 8-11 10-10-6-6 4z" stroke="#0e6570" stroke-width="2" fill="none" stroke-linejoin="round"/></svg><div><div class="stat-num">TOP 1.49%</div><div class="stat-cap">of All Agents in the USA</div></div></div>
  <div class="stat abs" style="top:2544px"><svg viewBox="0 0 44 44"><path d="M6 36V20L22 8l16 12v16zM17 36V26h10v10" stroke="#0e6570" stroke-width="2" fill="none" stroke-linejoin="round"/></svg><div><div class="stat-num">180+</div><div class="stat-cap">Deals Closed</div></div></div>
  <span class="side-label" style="left:1092px;top:2500px">Journey</span>
</section>

<section class="agent abs">
  <h2 class="heading agent-title abs">Meet Our <em>Expert Agent</em><br>The Philosophy</h2>
  <p class="body-text agent-text abs">Morbi tempus iaculis urna id volutpat lacus laoreet non curabitur gravida arcu ac tortor. Vitae congue mauris rhoncus aenean vel elit scelerisque mauris pellentesque pulvinar. Amet luctus venenatis lectus magna fringilla urna porttitor rhoncus dolor purus non enim praesent elementum facilisis leo vel fringilla est ullamcorper.</p>
  <p class="agent-name abs">Elias Wrenfield</p>
  <p class="agent-role abs">Property Expert</p>
  <div class="photo agent-photo abs" role="img" aria-label="Portrait of the property expert in a suit beside a modern apartment building"></div>
</section>

<section class="hood">
  <span class="side-label" style="left:72px;top:3700px">Neighborhood</span>
  <h2 class="heading hood-title abs">Discover Your Ideal<br><em>Neighborhood</em></h2>
  <div class="arrows abs">
    <span class="arrow on"><svg width="14" height="10" viewBox="0 0 14 10"><path d="M14 5H2M5 1L1 5l4 4" stroke="#fff" stroke-width="1.5" fill="none"/></svg></span>
    <span class="arrow"><svg width="14" height="10" viewBox="0 0 14 10"><path d="M0 5h12M9 1l4 4-4 4" stroke="#16181f" stroke-width="1.5" fill="none"/></svg></span>
  </div>
  <div class="hood-card abs" style="left:148px;width:412px;background:linear-gradient(180deg,#8fc3ec,#c9d8df 40%,#2aa8b8 70%,#1c7c92)" role="img" aria-label="Coastal city skyline above a turquoise bay"><span class="hood-name">Rutherford</span></div>
  <div class="hood-card abs" style="left:592px;width:416px;background:linear-gradient(180deg,#5a3f8a,#c65a9a 40%,#e59a6a 60%,#2a2f55)" role="img" aria-label="Waterfront city with a ferris wheel at sunset"><span class="hood-name">Kenwood</span></div>
  <div class="hood-card abs" style="left:1048px;width:200px;background:linear-gradient(180deg,#213052,#d27a3a 55%,#3a2a3c)" role="img" aria-label="City lights at dusk"><span class="hood-name">Yountville</span></div>
  <span class="btn hood-btn abs">View All Neighborhood <svg viewBox="0 0 18 10"><path d="M0 5h16M12 1l4 4-4 4" stroke="#fff" stroke-width="1.5" fill="none"/></svg></span>
</section>

<section class="news">
  <h2 class="heading news-title abs"><em>News</em> &amp; Insights</h2>
  <article class="news-card abs" style="left:148px">
    <div class="news-photo" role="img" aria-label="Brick house with a red tiled roof" style="background:linear-gradient(170deg,#7fb0df,#b8673e 50%,#4f7a36)"></div>
    <h3 class="news-head">Real Estate Market: Heads Up, Here's How Buyers Can Keep Their Cool</h3>
    <p class="news-date">June 15,2024</p>
  </article>
  <article class="news-card abs" style="left:460px">
    <div class="news-photo" role="img" aria-label="Couple holding a small model house" style="background:linear-gradient(170deg,#d9d4cc,#9c8670 55%,#e8e2d8)"></div>
    <h3 class="news-head">Real Estate Market: Heads Up, Here's How Buyers Can Keep Their Cool</h3>
    <p class="news-date">June 15,2024</p>
  </article>
  <article class="news-card abs" style="left:772px">
    <div class="news-photo" role="img" aria-label="Large house with a green roof among trees" style="background:linear-gradient(170deg,#8bb8e0,#3f6a4e 45%,#9a7b5c 70%,#5a8040)"></div>
    <h3 class="news-head">Real Estate Market: Heads Up, Here's How Buyers Can Keep Their Cool</h3>
    <p class="news-date">June 15,2024</p>
  </article>
</section>

<footer class="footer abs">
  <div class="brand"><span class="brand-dot"></span>ZP Real Estate</div>
  <div class="f-col" style="left:348px"><h4>Location</h4><p>1922 Quenby Row, Suite 193,<br>Harlow City, HC 40210</p></div>
  <div class="f-col" style="left:612px"><h4>Reach us</h4><p>Call : +1 (555) 014-7711<br>Email : hello@zprealestate.test</p></div>
  <div class="f-col" style="left:880px"><h4>Connect with us</h4><div class="socials"><span></span><span></span><span></span></div></div>
  <div class="f-bottom"><div class="links"><span>Home</span><span>About ZP</span><span>Properties</span><span>Terms &amp; Insights</span><span>Let's Connect</span></div><span class="copy">© 2024 ZP Real Estate. All rights reserved.</span></div>
</footer>

</body>
</html>
```